Einladungskarten für 30-jähriges Jubiläum
Zielgruppe
Wir sind ein Kompetenzzentrum für Gesundheit, Fitness und Regulationsmedizin. Im April 2024 feiern wir 30-jähriges Jubiläum. Wir haben in den Jahrzehnten viele Gesundheitsbewusste, Führungskräfte, Manager und Sportler betreut und uns als Mikronährstoffanalyse experten etabliert. Der Slogen 'Vitalität nach Maß' resuliert aus den Ergebnissen der speziellen Blutanalysen, die als Ergebnis Empfehlungen für Supplemente haben, zusammengestellt wie ein Kochrezept, deshalb 'Vitalität nach Maß'.
Aufgabenstellung
Eine seriöse SAFE THE DATE Karte (Formal ist egal) und daraus resultierend die Einladungskarte. Die Karten sollen per Post verschickt werden. Unsere Firmenfarben sind grün und blau. DIN-A-5 als Klappkarte für die Einladung wäre wünschenswert, da wir den Programmablauf mit aufnehmen möchten.

```html
<!DOCTYPE html>
<html lang="de">
<head>
<meta charset="utf-8">
<title>Einladung – 30 Jahre Jubiläum</title>
<link rel="stylesheet" href="https://fonts.googleapis.com/css2?family=Archivo+Black&family=Barlow+Condensed:wght@300;400;500;600&family=Jost:wght@400;600;700&display=swap">
<style>
  :root {
    --green: #6db753;
    --blue: #3e5fa9;
    --white: #ffffff;
    --paper: #ffffff;
    --rule: #d9d9d9;
  }
  * { margin: 0; padding: 0; box-sizing: border-box; }
  html, body { width: 1200px; height: 849px; overflow: hidden; background: var(--paper); }
  .card { position: relative; width: 1200px; height: 849px; overflow: hidden; }

  .cover-band { position: absolute; left: 0; top: 0; width: 1200px; height: 423px; background: var(--green); }

  .greeting {
    position: absolute; left: 0; width: 600px; top: 124px; text-align: center;
    font-family: "Barlow Condensed", sans-serif; font-weight: 300; font-size: 24px; color: var(--white);
  }

  .brand { position: absolute; text-align: center; color: var(--white); }
  .brand-name { font-family: "Jost", sans-serif; font-weight: 700; letter-spacing: 1px; line-height: 1; }
  .brand-tagline { font-family: "Jost", sans-serif; font-weight: 400; font-variant: small-caps; line-height: 1.45; }
  .brand--back { left: 0; width: 600px; top: 194px; }
  .brand--back .brand-name { font-size: 32px; }
  .brand--back .brand-tagline { font-size: 14px; margin-top: 8px; }
  .brand--front { left: 700px; width: 400px; top: 326px; }
  .brand--front .brand-name { font-size: 25px; }
  .brand--front .brand-tagline { font-size: 11px; margin-top: 5px; }

  .event-title { position: absolute; left: 700px; width: 400px; top: 140px; text-align: center; color: var(--white); }
  .event-title-name {
    font-family: "Jost", sans-serif; font-weight: 700; font-size: 40px; line-height: 1.1;
  }
  .event-title-sub {
    font-family: "Barlow Condensed", sans-serif; font-weight: 300; font-size: 26px; margin-top: 6px;
  }

  .confetti-field {
    position: absolute; left: 30px; top: 430px; width: 580px; height: 250px;
    background: radial-gradient(ellipse at center, rgba(109,183,83,0.07), rgba(109,183,83,0) 70%);
  }

  .anniversary { position: absolute; left: 0; width: 640px; top: 518px; text-align: center; }
  .anniversary-line1 {
    font-family: "Archivo Black", sans-serif; font-size: 39px; line-height: 1; color: var(--green); letter-spacing: 0.5px;
  }
  .anniversary-line2 {
    font-family: "Archivo Black", sans-serif; font-size: 54px; line-height: 1.05; color: var(--green);
  }

  .event-facts {
    position: absolute; left: 0; width: 640px; top: 618px; text-align: center;
    font-family: "Barlow Condensed", sans-serif; font-weight: 300; font-size: 21px; line-height: 27px; color: var(--blue);
  }
  .event-facts strong { font-weight: 600; }

  .balloon-row {
    position: absolute; left: 68px; top: 700px; width: 512px; height: 149px;
    background: linear-gradient(180deg, rgba(109,183,83,0.18), rgba(109,183,83,0.05));
    border-radius: 60px 60px 0 0;
  }

  .programme { position: absolute; left: 673px; top: 452px; width: 470px; color: var(--blue); }
  .programme-title {
    font-family: "Archivo Black", sans-serif; font-size: 27px; line-height: 1; color: var(--green); letter-spacing: 0.5px;
  }
  .programme-subtitle {
    font-family: "Barlow Condensed", sans-serif; font-weight: 300; font-size: 22px; margin-top: 8px;
  }
  .programme-item { margin-top: 16px; }
  .programme-item + .programme-item { margin-top: 29px; }
  .programme-item h3 {
    font-family: "Jost", sans-serif; font-weight: 700; font-size: 15px; letter-spacing: 0.3px; line-height: 1.2;
  }
  .programme-item p {
    font-family: "Barlow Condensed", sans-serif; font-weight: 300; font-size: 16.5px; line-height: 19.3px; margin-top: 2px;
  }

  .fold-rule { position: absolute; left: 0; top: 846px; width: 1045px; height: 3px; background: var(--rule); }
</style>
</head>
<body>
<main class="card">
  <div class="cover-band"></div>

  <p class="greeting">Wir freuen uns auf Euch!</p>

  <div class="brand brand--back">
    <div class="brand-name">VITANOVA</div>
    <div class="brand-tagline">Ihr Zentrum für Vitalität<br>und Bewegung im ganzen Land</div>
  </div>

  <div class="event-title">
    <div class="event-title-name">Vitalität nach Maß</div>
    <div class="event-title-sub">Wirtschafts- &amp; Gesundheitsforum</div>
  </div>

  <div class="brand brand--front">
    <div class="brand-name">VITANOVA</div>
    <div class="brand-tagline">Ihr Zentrum für Vitalität<br>und Bewegung im ganzen Land</div>
  </div>

  <div class="confetti-field" role="img" aria-label="Grünes Konfetti als festliche Dekoration"></div>

  <div class="anniversary">
    <div class="anniversary-line1">WIR WERDEN</div>
    <div class="anniversary-line2">30 JAHRE</div>
  </div>

  <div class="event-facts">
    <p><strong>Wann?</strong> Mittwoch, 10. April 2024 um 18.00 Uhr</p>
    <p><strong>Wo?</strong> Sternensaal; Parkhalle in Lindenau/Westfalen</p>
  </div>

  <div class="balloon-row" role="img" aria-label="Reihe aus fünf grünen Luftballons"></div>

  <section class="programme">
    <h2 class="programme-title">PROGRAMM</h2>
    <p class="programme-subtitle">Wirtschafts- und Gesundheitsforum „Vitalität nach Maß“</p>
    <div class="programme-item">
      <h3>ÜBERSCHRIFT 1</h3>
      <p>Ortus conscris nonerte, crum vivescem deo, us aus auceper avenihilin diem simunte tem di publica tiam faut audeti, conloctus praes publia ca; Catque re, que vis intem meniam ut vignatere id re, denatiamquam medem</p>
    </div>
    <div class="programme-item">
      <h3>ÜBERSCHRIFT 2</h3>
      <p>Ortus conscris nonerte, crum vivescem deo, us aus auceper avenihilin diem simunte tem di publica tiam faut audeti, conloctus praes publia ca; Catque re, que vis intem meniam ut vignatere id re, denatiamquam medem</p>
    </div>
    <div class="programme-item">
      <h3>ÜBERSCHRIFT 3</h3>
      <p>Ortus conscris nonerte, crum vivescem deo, us aus auceper avenihilin diem simunte tem di publica tiam faut audeti, conloctus praes publia ca; Catque re, que vis intem meniam ut vignatere id re, denatiamquam medem</p>
    </div>
  </section>

  <div class="fold-rule"></div>
</main>
</body>
</html>
```